Flyer for a marketing

We are a holistic mental health facility in need of a flyer to help promote our services and encourage more people to seek care. See the attachment to tell you more. We prefer warm green colors or rich blue. Thank you.

```html
<!DOCTYPE html>
<html lang="en">
<head>
<meta charset="utf-8">
<title>Evergreen Mind Health and Wellness – Flyer</title>
<link href="https://fonts.googleapis.com/css2?family=Noto+Serif:wght@700&family=Red+Hat+Display:wght@500;600&display=swap" rel="stylesheet">
<style>
  :root{
    --green-dark:#0e5229;
    --green-brand:#1f6e3a;
    --green-mid:#4f8f3e;
    --green-light:#5a9a45;
    --orange:#f0a023;
    --ink:#333333;
    --paper:#ffffff;
    --backdrop:#e9e6df;
  }
  *{box-sizing:border-box;margin:0;padding:0}
  html,body{width:1200px;height:1117px;overflow:hidden;background:var(--backdrop)}
  .flyer{position:absolute;left:220px;top:20px;width:760px;height:1076px;background:var(--paper);overflow:hidden;font-family:"Red Hat Display",Arial,sans-serif;box-shadow:0 4px 18px rgba(0,0,0,.18)}
  .layer{position:absolute;left:0;top:0;width:760px;height:1076px}
  .accent-dots{position:absolute;left:40px;top:40px;width:46px;height:112px;background:rgba(240,160,35,.18);border-radius:4px}
  .brand-mark{position:absolute;left:140px;top:70px;width:150px;height:150px;border-radius:50%;background:var(--green-brand)}
  .brand-divider{position:absolute;left:375px;top:23px;width:4px;height:237px;background:var(--green-brand)}
  .brand-name{position:absolute;left:426px;top:38px;font-family:"Noto Serif",Georgia,serif;font-weight:700;font-size:36px;line-height:40.5px;color:var(--green-brand)}
  .headline{position:absolute;left:63px;top:270px;font-family:"Noto Serif",Georgia,serif;font-weight:700;font-size:42px;letter-spacing:-.5px;color:var(--orange)}
  .tagline{position:absolute;left:50px;top:320px;width:420px;text-align:center;font-size:17px;line-height:19.5px;color:var(--ink)}
  .benefits{position:absolute;left:32px;top:395px;width:530px;height:337px;border:3px solid var(--orange);border-radius:22px;background:var(--paper);box-shadow:-6px 6px 0 #d9d9d9}
  .benefits-title{position:absolute;left:29px;top:17px;width:306px;height:43px;border-radius:22px;background:var(--green-mid);color:#fff;font-family:"Noto Serif",Georgia,serif;font-weight:700;font-size:29px;line-height:43px;text-align:center}
  .benefits-list{position:absolute;left:30px;top:74px;width:290px;list-style:none}
  .benefits-list li{position:relative;padding-left:24px;font-size:15.5px;line-height:17.5px;color:var(--ink);margin-bottom:16px}
  .benefits-list svg{position:absolute;left:0;top:2px;width:14px;height:14px}
  .cta{position:absolute;left:0;top:762px;width:760px;text-align:center;color:#fff}
  .cta-title{font-family:"Noto Serif",Georgia,serif;font-weight:700;font-size:39px;line-height:41px}
  .cta-note{font-family:"Noto Serif",Georgia,serif;font-weight:700;font-size:12.5px;margin-top:6px}
  .contact{position:absolute;left:100px;top:918px;color:#fff;font-family:"Noto Serif",Georgia,serif;font-weight:700}
  .contact-company{font-size:23px;color:var(--orange);margin-bottom:10px}
  .contact-grid{position:relative;width:560px;font-size:17px}
  .contact-row{display:flex;align-items:center;height:31px}
  .contact-row svg{width:17px;height:17px;margin-right:8px;flex:none}
  .contact-col-right{position:absolute;left:240px;top:0}
  .contact-divider{position:absolute;left:212px;top:2px;width:2px;height:54px;background:#fff}
</style>
</head>
<body>
<main class="flyer">
  <svg class="layer" viewBox="0 0 760 1076" aria-hidden="true">
    <defs>
      <linearGradient id="bandGreen" x1="0" y1="0" x2="0" y2="1">
        <stop offset="0" stop-color="#3d7f37"/><stop offset="1" stop-color="#5a9a45"/>
      </linearGradient>
    </defs>
    <path d="M0,555 Q15,545 30,545 L30,740 L760,740 L760,1076 L0,1076Z" fill="url(#bandGreen)"/>
    <path d="M0,925 C150,872 330,875 480,888 C620,898 700,860 760,815 L760,1076 L0,1076Z" fill="var(--green-dark)"/>
  </svg>

  <div class="accent-dots" role="img" aria-label="Small orange dot grid decoration"></div>
  <div class="brand-mark"></div>
  <div class="brand-divider"></div>
  <h1 class="brand-name">Evergreen<br>Mind<br>Health<br>and<br>Wellness</h1>

  <h2 class="headline">The Care You Deserve</h2>
  <p class="tagline">Evergreen Mind Health and Wellness, where deserving patients meet compassionate providers.</p>

  <section class="benefits">
    <div class="benefits-title">Why Choose Us?</div>
    <ul class="benefits-list">
      <li><svg viewBox="0 0 14 14"><circle cx="7" cy="7" r="7" fill="#1f6e3a"/><path d="M3.8,7.2 6,9.3 10.2,4.9" stroke="#fff" stroke-width="1.8" fill="none"/></svg>We are an integrative holistic psychiatric center.</li>
      <li><svg viewBox="0 0 14 14"><circle cx="7" cy="7" r="7" fill="#1f6e3a"/><path d="M3.8,7.2 6,9.3 10.2,4.9" stroke="#fff" stroke-width="1.8" fill="none"/></svg>Our mission is to provide compassionate quality care.</li>
      <li><svg viewBox="0 0 14 14"><circle cx="7" cy="7" r="7" fill="#1f6e3a"/><path d="M3.8,7.2 6,9.3 10.2,4.9" stroke="#fff" stroke-width="1.8" fill="none"/></svg>We provide psychiatric services including medication management and psychotherapy.</li>
      <li><svg viewBox="0 0 14 14"><circle cx="7" cy="7" r="7" fill="#1f6e3a"/><path d="M3.8,7.2 6,9.3 10.2,4.9" stroke="#fff" stroke-width="1.8" fill="none"/></svg>We listen, care, and empower you to live better.</li>
      <li><svg viewBox="0 0 14 14"><circle cx="7" cy="7" r="7" fill="#1f6e3a"/><path d="M3.8,7.2 6,9.3 10.2,4.9" stroke="#fff" stroke-width="1.8" fill="none"/></svg>We accept major insurances.</li>
    </ul>
  </section>

  <svg class="layer" viewBox="0 0 760 1076">
    <defs>
      <linearGradient id="ringOrange" x1="0" y1="0" x2="1" y2="1">
        <stop offset="0" stop-color="#f0a023"/><stop offset=".45" stop-color="#fbd9a0"/><stop offset=".6" stop-color="#f0a023"/><stop offset="1" stop-color="#f3b04a"/>
      </linearGradient>
      <linearGradient id="photoTone" x1="0" y1="0" x2="1" y2="1">
        <stop offset="0" stop-color="#b9a48c"/><stop offset=".5" stop-color="#8a7666"/><stop offset="1" stop-color="#c9c6c2"/>
      </linearGradient>
    </defs>
    <path d="M760,232 C610,300 420,380 370,530 C470,405 620,330 760,300Z" fill="var(--green-mid)"/>
    <ellipse cx="668" cy="530" rx="290" ry="222" fill="var(--paper)"/>
    <ellipse cx="668" cy="530" rx="282" ry="216" fill="none" stroke="url(#ringOrange)" stroke-width="16"/>
    <ellipse cx="672" cy="528" rx="266" ry="202" fill="url(#photoTone)" role="img" aria-label="Photo of a woman at home rubbing her neck, looking tired and stressed"/>
  </svg>

  <section class="cta">
    <p class="cta-title">We are accepting new patients,<br>no waiting list.</p>
    <p class="cta-note">Your mental health matters, so make it a priority and call us today for an appointment.</p>
  </section>

  <section class="contact">
    <p class="contact-company">Evergreen Mind Health and Wellness, APNC</p>
    <div class="contact-grid">
      <div class="contact-row"><svg viewBox="0 0 17 17"><circle cx="8.5" cy="8.5" r="8.5" fill="#fff"/><path d="M5.5,4.5 7,4.3 7.8,6.6 6.8,7.4 Q7.6,9.3 9.6,10.2 L10.4,9.2 12.7,10 12.5,11.5 Q8,12.3 5,7.6Z" fill="#0e5229"/></svg>Ph (555) 204-7318</div>
      <div class="contact-row"><svg viewBox="0 0 17 17"><circle cx="8.5" cy="8.5" r="8.5" fill="#fff"/><rect x="6" y="4" width="5" height="3" fill="#0e5229"/><rect x="4" y="7" width="9" height="4" rx="1" fill="#0e5229"/><rect x="6" y="10" width="5" height="3" fill="#0e5229"/></svg>Fax (555) 610-4427</div>
      <div class="contact-row"><svg viewBox="0 0 17 17"><path d="M8.5,1 C4.8,1 2.8,3.6 2.8,6.4 C2.8,10 8.5,16 8.5,16 C8.5,16 14.2,10 14.2,6.4 C14.2,3.6 12.2,1 8.5,1Z" fill="#fff"/><circle cx="8.5" cy="6.3" r="2.2" fill="#0e5229"/></svg>1480 Cedar Hollow Road, Suite 200 Maple Falls, CA 90000</div>
      <div class="contact-divider"></div>
      <div class="contact-col-right">
        <div class="contact-row"><svg viewBox="0 0 17 17"><circle cx="8.5" cy="8.5" r="8.5" fill="#fff"/><rect x="4" y="5.5" width="9" height="6" fill="none" stroke="#0e5229" stroke-width="1.2"/><path d="M4,5.5 8.5,9 13,5.5" fill="none" stroke="#0e5229" stroke-width="1.2"/></svg>info@evergreenmindhealth.com</div>
        <div class="contact-row"><svg viewBox="0 0 17 17"><circle cx="8.5" cy="8.5" r="8.5" fill="#fff"/><circle cx="8.5" cy="8.5" r="4.8" fill="none" stroke="#0e5229" stroke-width="1.1"/><ellipse cx="8.5" cy="8.5" rx="2" ry="4.8" fill="none" stroke="#0e5229" stroke-width="1.1"/><path d="M3.7,8.5 H13.3" stroke="#0e5229" stroke-width="1.1"/></svg>evergreenmindhealth.com</div>
      </div>
    </div>
  </section>
</main>
</body>
</html>
```